letter head for a construction company

Company Name: Zaviro Construction Limited

Address: Kilele Street, Tengeru Shores, Dar es salaam, Tanzania

Phone: 0754382916

email : info@zaviroconstruction.example

website : www.zaviroconstruction.example

```html
<!DOCTYPE html>
<html lang="en">
<head>
<meta charset="utf-8">
<title>Zaviro Construction Limited – Letterhead</title>
<link href="https://fonts.googleapis.com/css2?family=Lato:wght@400;700;900&family=Allura&display=swap" rel="stylesheet">
<style>
  :root {
    --backdrop: #e6e6e8;
    --paper: #ffffff;
    --ink: #3a3a3c;
    --ink-soft: #55565a;
    --charcoal: #454547;
    --orange: #ef7d14;
  }
  * { box-sizing: border-box; margin: 0; padding: 0; }
  html, body {
    width: 1200px; height: 874px; overflow: hidden;
    background: var(--backdrop);
    font-family: "Lato", Arial, sans-serif;
    color: var(--ink);
  }
  .letterhead {
    position: absolute; left: 308px; top: 24px;
    width: 584px; height: 826px;
    background: var(--paper);
    box-shadow: 0 4px 18px rgba(0,0,0,.12);
    overflow: hidden;
  }
  .brand {
    position: absolute; left: 46px; top: 70px;
    font-family: "Lato", Arial, sans-serif;
    font-weight: 700; color: var(--ink);
    display: flex; align-items: center; gap: 10px;
  }
  .brand-mark { width: 14px; height: 14px; background: var(--ink); }
  .brand-name { font-size: 30px; letter-spacing: 1px; line-height: 1; }
  .brand-sub { font-size: 9.5px; letter-spacing: 5.2px; margin-top: 4px; }

  .contact {
    position: absolute; left: 352px; top: 58px;
    padding-left: 14px;
    border-left: 1px solid var(--orange);
    font-size: 8.6px; line-height: 1.45; color: var(--ink);
  }
  .contact-company { font-weight: 900; font-size: 8.4px; text-transform: uppercase; }
  .contact-company .accent { color: var(--orange); }
  .contact-line { display: flex; align-items: center; gap: 6px; }
  .contact-icon { width: 8px; height: 8px; flex: none; }

  .letter {
    position: absolute; left: 46px; top: 200px; width: 470px;
    font-size: 9.6px; line-height: 1.55; color: var(--ink-soft);
  }
  .letter-date { margin-bottom: 12px; }
  .letter-recipient { margin-bottom: 12px; }
  .letter-address { margin-bottom: 16px; }
  .letter-salutation { font-weight: 900; font-size: 12px; color: var(--ink); margin-bottom: 12px; }
  .letter p.body { margin-bottom: 14px; }
  .letter-closing { margin-top: 26px; }
  .letter-signature {
    font-family: "Allura", cursive;
    font-size: 34px; color: #2a2a2a; margin-top: 6px; margin-left: 24px;
  }
  .footer-wave { position: absolute; left: 0; bottom: 0; width: 584px; height: 826px; }
</style>
</head>
<body>
  <main class="letterhead">
    <div class="brand">
      <span class="brand-mark"></span>
      <div>
        <div class="brand-name">ZAVIRO</div>
        <div class="brand-sub">CONSTRUCTION LTD</div>
      </div>
    </div>

    <address class="contact" style="font-style:normal">
      <div class="contact-company">Zaviro <span class="accent">Construction</span> Limited</div>
      <div>Kilele Street, Tengeru Shores,</div>
      <div>Dar es salaam, Tanzania</div>
      <div class="contact-line">
        <svg class="contact-icon" viewBox="0 0 10 10"><path fill="#ef7d14" d="M2 1l2 2-1 1.5c.6 1.2 1.3 1.9 2.5 2.5L7 6l2 2-1.5 1.5C4.5 9 1 5.5.5 2.5z"/></svg>
        <span>0754382916</span>
      </div>
      <div class="contact-line">
        <svg class="contact-icon" viewBox="0 0 10 10"><rect x="0.5" y="2" width="9" height="6.5" fill="#ef7d14"/><path d="M.5 2l4.5 3.5L9.5 2" fill="none" stroke="#fff" stroke-width=".9"/></svg>
        <span>info@zaviroconstruction.example</span>
      </div>
      <div class="contact-line">
        <svg class="contact-icon" viewBox="0 0 10 10"><circle cx="5" cy="5" r="4.5" fill="#ef7d14"/><path d="M.5 5h9M5 .5c-2.2 2.5-2.2 6.5 0 9M5 .5c2.2 2.5 2.2 6.5 0 9" fill="none" stroke="#fff" stroke-width=".7"/></svg>
        <span>www.zaviroconstruction.example</span>
      </div>
    </address>

    <section class="letter">
      <div class="letter-date">Feb-03-2022</div>
      <div class="letter-recipient">Mr. Peter Lema<br>President</div>
      <div class="letter-address">Harborline Group<br>123 Street Name, Suite# 10<br>City, State, 120023</div>
      <div class="letter-salutation">Dear Mr. Peter</div>
      <p class="body">Lorem ipsum dolor sit amet, consectetur adipisicing elit, sed do eiusmod tempor incididunt ut labore et dolore magna aliqua. Ut enim ad minim veniam, quis nostrud exercitation ullamco laboris nisi ut aliquip ex ea commodo consequat. Duis aute irure dolor in reprehenderit in voluptate velit esse cillum dolore eu fugiat nulla pariatur.</p>
      <p class="body">Lorem ipsum dolor sit amet, consectetur adipisicing elit, sed do eiusmod tempor incididunt ut labore et dolore magna aliqua. Ut enim ad minim veniam, quis nostrud exercitation ullamco laboris nisi ut aliquip ex ea commodo consequat. Duis aute irure dolor in reprehenderit in voluptate velit esse cillum dolore eu fugiat nulla pariatur.</p>
      <p class="body">Lorem ipsum dolor sit amet, consectetur adipisicing elit, sed do eiusmod tempor incididunt ut labore et dolore magna aliqua. Ut enim ad minim veniam, quis nostrud exercitation ullamco laboris nisi ut aliquip ex ea commodo consequat.</p>
      <p class="body">Excepteur sint occaecat cupidatat non proident, sunt in culpa qui officia deserunt mollit anim id est laborum. re et dolore magnam aliquam quaerat voluptatem.</p>
      <div class="letter-closing">Regards</div>
      <div class="letter-signature">Daniel Mushi</div>
    </section>

    <svg class="footer-wave" viewBox="0 0 584 826" aria-hidden="true">
      <path fill="var(--charcoal)" d="M205 826 C330 826 380 770 440 705 C495 645 540 615 584 602 L584 826 Z"/>
      <path fill="var(--orange)" d="M255 812 C360 798 405 742 455 688 C500 640 540 612 580 598 C545 616 508 648 462 698 C412 752 368 800 255 812 Z"/>
    </svg>
  </main>
</body>
</html>
```